Breezy Lanterns Handcrafted Copper Jewelry

I make handcrafted copper bracelets and cuffs.
I need a banner made (2' 1/2" x 10')
I attached the logo (I would like that sketch to be purple)
Company name: Breezy Lanterns (in a "sassy" font)
Tag line: Bring the Breeze
Designer/Creator: Marla Dunsby
481.307.6624
FB: www.facebook.com/breezylanterns.net
shop.breezylanterns.net
I'd like the background to be white. I'm not sure what I'm looking for as far as the look or if I should add any pics of the copper jewelry that I make. I'm totally up for suggestions. I'm very eager to see how creative you can be.
Many thanks.

```html
<!DOCTYPE html>
<html lang="en">
<head>
<meta charset="utf-8">
<title>Breezy Lanterns Banner</title>
<link href="https://fonts.googleapis.com/css2?family=Oleo+Script&family=Mulish:wght@300;400&display=swap" rel="stylesheet">
<style>
  :root {
    --page: #f4f1ee;
    --pink-light: #f9d3e6;
    --pink-mid: #f3b4d4;
    --pink-deep: #ee9cc6;
    --purple: #6b3d9e;
  }
  html, body {
    margin: 0;
    width: 1200px;
    height: 1000px;
    overflow: hidden;
    background: var(--page);
  }
  .banner {
    position: absolute;
    left: 80px;
    top: 370px;
    width: 1040px;
    height: 260px;
    background:
      radial-gradient(circle at 20% 30%, var(--pink-light) 0, transparent 45%),
      radial-gradient(circle at 75% 70%, var(--pink-light) 0, transparent 40%),
      linear-gradient(135deg, var(--pink-mid), var(--pink-deep) 60%, var(--pink-mid));
    color: var(--purple);
    font-family: "Mulish", sans-serif;
  }
  .tagline {
    position: absolute;
    left: 48px;
    top: 78px;
    margin: 0;
    font-family: "Oleo Script", cursive;
    font-weight: 400;
    font-size: 74px;
    line-height: 1;
    letter-spacing: 1px;
    text-shadow: 1px 2px 3px rgba(90, 40, 120, 0.25);
  }
  .brand-name {
    position: absolute;
    left: 612px;
    top: 112px;
    width: 170px;
    margin: 0;
    font-family: "Oleo Script", cursive;
    font-size: 32px;
    line-height: 1.05;
    text-align: center;
  }
  .creator {
    position: absolute;
    left: 770px;
    top: 98px;
    font-family: "Oleo Script", cursive;
    font-size: 26px;
  }
  .contact {
    position: absolute;
    top: 236px;
    margin: 0;
    font-size: 19px;
    font-weight: 300;
    line-height: 1;
    transform: translateY(-50%);
    display: flex;
    align-items: center;
    gap: 6px;
  }
  .contact-phone { left: 80px; }
  .contact-social { left: 322px; }
  .contact-shop { right: 38px; }
  .social-dot {
    width: 22px;
    height: 22px;
    border-radius: 50%;
    background: var(--purple);
  }
</style>
</head>
<body>
  <section class="banner">
    <h1 class="tagline">Bring the Breeze</h1>
    <p class="brand-name">Breezy Lanterns</p>
    <span class="creator">by Marla Dunsby</span>
    <p class="contact contact-phone">481.307.6624</p>
    <p class="contact contact-social"><span class="social-dot"></span>breezylanterns.net</p>
    <p class="contact contact-shop">www.shop.breezylanterns.net</p>
  </section>
</body>
</html>
```